ZEPHIRO needs a new business card!

ZEPHIRO is a group of gaming enthusiasts who are looking for a new corporate business card.

The typeface should be modern and minimalist with attention paid to spacing between the letters and the letters 'zephiro' look relative to each other.

Should clean, crisp and minimalist - looking serious overall but with slight tweaks to the letters to make them look playful...

Black on white is fine.

Details on the card should include:
-the word 'zephiro'
-a job title (use any, for e.g. founder)
-a name (e.g. Ned Falka)
-phone number
-email address

For inspiration: http://brisket.tumblevane-cdn.example/wp-content/uploads/2013/07/mela-1.jpg

Target Market(s)

Video gaming enthusiasts

Industry/Entity Type

Business

Requirements
Must have
• Black letter on white background.
The word "zephiro"
Nice to have
• Maybe use a conservative font like Gibraltar or Helvetica and tweaking each letter individually.

You can insert normal job titles under the "zephiro" typeface
Should not have
• Should not be cartoony or childish fonts. No colors.

```html
<!DOCTYPE html>
<html lang="en">
<head>
<meta charset="utf-8">
<title>ZEPHIRO business card</title>
<link rel="stylesheet" href="https://fonts.googleapis.com/css2?family=Jost:wght@700&family=Questrial&display=swap">
<style>
  :root {
    --backdrop: #3a3a3a;
    --card: #ffffff;
    --ink: #000000;
    --muted: #6b6b6b;
    --band: #cfcfcf;
  }
  * { margin: 0; padding: 0; box-sizing: border-box; }
  html, body { width: 1200px; height: 1001px; overflow: hidden; }
  body {
    background: var(--backdrop);
    display: flex;
    align-items: center;
    justify-content: center;
    font-family: "Questrial", "Century Gothic", sans-serif;
  }
  .card {
    position: relative;
    width: 340px;
    height: 580px;
    background: var(--card);
    border-radius: 24px;
  }
  .wordmark {
    position: absolute;
    top: 190px;
    left: 0;
    right: 0;
    text-align: center;
    font-family: "Jost", "Futura", sans-serif;
    font-weight: 700;
    font-size: 58px;
    letter-spacing: 1px;
    color: var(--ink);
  }
  .title-band {
    position: absolute;
    top: 400px;
    left: 90px;
    right: 0;
    height: 30px;
    background: var(--band);
  }
  .job-title {
    position: absolute;
    top: 382px;
    right: 22px;
    font-size: 15px;
    color: var(--muted);
  }
  .contact-list {
    position: absolute;
    top: 448px;
    right: 22px;
    list-style: none;
    text-align: right;
    font-size: 14px;
    line-height: 22px;
    color: var(--muted);
  }
  .contact-icons {
    position: absolute;
    top: 405px;
    left: 22px;
    display: flex;
    flex-direction: column;
    gap: 8px;
  }
  .contact-icons svg { display: block; width: 16px; height: 16px; }
</style>
</head>
<body>
  <section class="card" aria-label="ZEPHIRO business card">
    <div class="wordmark">ZEPHIRO</div>
    <div class="title-band"></div>
    <p class="job-title">product manager</p>
    <div class="contact-icons">
      <svg class="icon-phone" viewBox="0 0 16 16" aria-hidden="true">
        <rect x="4" y="1" width="8" height="14" rx="2" fill="none" stroke="#6b6b6b" stroke-width="1.6"/>
        <circle cx="8" cy="12.2" r="0.9" fill="#6b6b6b"/>
      </svg>
      <svg class="icon-mail" viewBox="0 0 16 16" aria-hidden="true">
        <rect x="1" y="3" width="14" height="10" rx="1.5" fill="#6b6b6b"/>
        <path d="M2 4 L8 9 L14 4" fill="none" stroke="#ffffff" stroke-width="1.3"/>
      </svg>
      <svg class="icon-social" viewBox="0 0 16 16" aria-hidden="true">
        <rect x="1" y="1" width="14" height="14" rx="3" fill="#6b6b6b"/>
      </svg>
    </div>
    <ul class="contact-list">
      <li>+ 34&nbsp; 5120 48391 207</li>
      <li>zephiro@orbitmail.com</li>
      <li>playnet.com/zephiro</li>
    </ul>
  </section>
</body>
</html>
```